Website Landing Page for Medical Recruitment

Looking for a landing page to add to our existing website. The objective of the page is to recruit new clinical staff for various departments within Larkfield Medical Center (non-profit hospital in the Richmond, TX area).

We would like the page to be modern, professional, and non-cluttered. Please include call-to-actions and include a button that will navigate to the page where candidates can submit their applications (this page already exists).

Target Market(s)

25-35-year-olds who live in the Houston and Richmond area with medical experience.

Industry/Entity Type

Medical/Health

Font styles to use
Sans Serif

Colors
0054AA
0677BA
7BADD7
CADEEF
E8F1F8

Requirements
Must have
• A "call to action"; a button that navigates to larkfieldmedhub.example/careers

```html
<!DOCTYPE html>
<html lang="en">
<head>
<meta charset="utf-8">
<title>Larkfield Medical Center – Careers</title>
<link href="https://fonts.googleapis.com/css2?family=Poppins:wght@400;500;600;700&display=swap" rel="stylesheet">
<style>
:root{
  --blue-deep:#0054AA;
  --blue:#2a5fa3;
  --blue-mid:#0677BA;
  --blue-soft:#7BADD7;
  --blue-pale:#CADEEF;
  --blue-mist:#E8F1F8;
  --ink:#1f1f1f;
  --text:#6b6b6b;
  --white:#fff;
}
*{margin:0;padding:0;box-sizing:border-box}
html,body{width:1200px;height:3314px;overflow:hidden}
body{position:relative;font-family:'Poppins',sans-serif;color:var(--text);background:var(--white)}
a{text-decoration:none;color:inherit}
.abs{position:absolute}
.btn{position:absolute;display:flex;align-items:center;justify-content:center;background:var(--blue);color:var(--white);font-weight:600;font-size:15px;border-radius:30px;letter-spacing:.3px}
.brand{position:absolute;display:flex;align-items:center;gap:10px;color:var(--blue);font-weight:500;font-size:30px;letter-spacing:.5px}
.brand .dot{width:34px;height:34px;border-radius:50%;background:var(--blue)}
.brand small{display:block;font-size:11px;letter-spacing:1px;line-height:1;margin-top:-4px}

/* hero */
.hero-bg{position:absolute;left:0;top:0;width:1200px;height:1297px;background:linear-gradient(180deg,#eef3fa 0%,#e6eef8 60%,#dde8f5 100%)}
.nav a{position:absolute;top:36px;font-size:13px;color:#666}
.nav a.active{color:var(--blue)}
.hero-title{left:62px;top:240px;font-size:53px;line-height:68px;font-weight:600;color:var(--ink)}
.hero-text{left:61px;top:388px;width:430px;font-size:12.5px;line-height:22.5px}
.photo{position:absolute;background:linear-gradient(160deg,#c9dcf0 0%,#5c9ad8 55%,#1f6fc4 100%)}

/* jobs */
.section-title{position:absolute;left:0;width:1200px;text-align:center;font-size:37px;font-weight:600;color:var(--ink)}
.job{position:absolute;top:900px;width:248px;height:225px;background:var(--white);border-radius:3px;padding:26px 22px}
.job h3{font-size:15.5px;font-weight:600;color:var(--ink)}
.job .sub{font-size:13.5px;color:var(--blue);margin-top:4px}
.job p{font-size:12.5px;line-height:22.5px;margin-top:18px}
.job .link{position:absolute;left:23px;top:168px;font-size:11.5px;font-weight:600;color:var(--blue)}

/* about */
.about-bg{position:absolute;left:0;top:1297px;width:1200px;height:850px;background:linear-gradient(180deg,#fff 0%,#fff 45%,#e8f0f9 100%)}
.tile{position:absolute;width:150px;height:164px;border-radius:3px;color:var(--white);text-align:center;padding-top:36px}
.tile svg{width:40px;height:40px;opacity:.55}
.tile h4{font-size:14px;font-weight:600;margin-top:6px}
.tile p{font-size:10.5px;margin-top:1px;opacity:.9}
.about-title{left:640px;top:1470px;font-size:38px;font-weight:600;color:var(--ink)}
.about-text{left:638px;width:440px;font-size:12.5px;line-height:22.5px}

/* banner */
.banner{position:absolute;left:60px;top:2062px;width:1080px;height:187px;background:var(--blue);border-radius:3px;color:var(--white)}
.banner .circle{position:absolute;left:26px;top:14px;width:170px;height:170px;border-radius:50%;background:var(--white)}
.banner .rule{position:absolute;left:242px;top:20px;width:1px;height:150px;background:rgba(255,255,255,.12)}
.banner h2{position:absolute;left:280px;top:22px;font-size:30px;font-weight:600;letter-spacing:.3px}
.banner p{position:absolute;left:280px;top:68px;width:760px;font-size:12.5px;line-height:22.5px}
.banner .btn{left:280px;top:115px;width:150px;height:44px;background:var(--white);color:var(--blue)}

/* news */
.news{position:absolute;top:2424px;width:338px}
.news .img{height:224px;background:linear-gradient(150deg,#d9dde3 0%,#8a99ad 60%,#56657a 100%)}
.news .date{position:absolute;left:0;top:0;width:52px;height:52px;background:var(--blue);color:var(--white);text-align:center;padding-top:5px}
.news .date b{display:block;font-size:17px;font-weight:600;line-height:20px}
.news .date span{font-size:12px}
.news h3{font-size:12.5px;font-weight:600;color:var(--ink);line-height:22.5px;margin-top:20px;padding-left:2px}
.news p{font-size:12.5px;line-height:22.5px;margin-top:12px;padding-left:2px}
.news .link{display:block;font-size:11.5px;font-weight:600;color:var(--blue);margin-top:24px;padding-left:2px}

/* footer */
.footer-head{position:absolute;top:3052px;font-size:12.5px;font-weight:600;color:var(--ink)}
.footer-link{position:absolute;font-size:12.5px;color:#666}
.social{position:absolute;top:3188px;width:30px;height:30px;border-radius:50%;background:var(--blue)}
.newsletter{position:absolute;left:891px;top:3157px;width:249px;height:46px;border:1px solid #ccd6e3;border-radius:25px;background:var(--white);overflow:hidden}
.newsletter span{position:absolute;left:22px;top:14px;font-size:11px;color:#666}
.newsletter .send{position:absolute;right:0;top:0;width:52px;height:46px;background:var(--blue);display:flex;align-items:center;justify-content:center}
</style>
</head>
<body>

<!-- HERO -->
<div class="hero-bg"></div>
<svg class="abs" style="left:0;top:0" width="1200" height="905" viewBox="0 0 1200 905">
  <path d="M795 0 C590 230 455 470 640 600 L1200 905 L1200 0 Z" fill="#ffffff"/>
</svg>
<div class="photo" role="img" aria-label="Smiling nurse in blue scrubs with a stethoscope giving a thumbs up" style="left:575px;top:70px;width:605px;height:745px;border-radius:300px 300px 40px 40px"></div>

<div class="brand" style="left:60px;top:16px"><span class="dot"></span><div>Larkfield<small>MEDICAL CENTER</small></div></div>
<nav class="nav">
  <a class="active" style="left:612px">Home</a>
  <a style="left:683px">About Us</a>
  <a style="left:775px">Vacancies</a>
  <a style="left:877px">Contact Us</a>
</nav>
<a class="btn" href="https://larkfieldmedhub.example/careers" style="left:990px;top:24px;width:150px;height:45px">APPLY NOW</a>

<h1 class="abs hero-title">NEW OFFERS ARE<br>WAITING FOR YOU</h1>
<p class="abs hero-text">Lorem Ipsum is simply dummy text of the printing and typesetting industry. Lorem Ipsum has been the industry's standard dummy text ever since the 1500s.</p>
<a class="btn" href="https://larkfieldmedhub.example/careers" style="left:60px;top:477px;width:150px;height:44px">APPLY NOW</a>

<!-- JOB OFFERS -->
<h2 class="section-title" style="top:813px;left:-47px">JOB OFFERS</h2>
<div class="job" style="left:60px"><h3>Job Position</h3><div class="sub">Lorem ipsum</div><p>Lorem ipsum is simply dummy text and printing typesetting.</p><a class="link" href="https://larkfieldmedhub.example/careers">APPLY NOW</a></div>
<div class="job" style="left:338px"><h3>Job Position</h3><div class="sub">Lorem ipsum</div><p>Lorem ipsum is simply dummy text and printing typesetting.</p><a class="link" href="https://larkfieldmedhub.example/careers">APPLY NOW</a></div>
<div class="job" style="left:615px"><h3>Job Position</h3><div class="sub">Lorem ipsum</div><p>Lorem ipsum is simply dummy text and printing typesetting.</p><a class="link" href="https://larkfieldmedhub.example/careers">APPLY NOW</a></div>
<div class="job" style="left:892px"><h3>Job Position</h3><div class="sub">Lorem ipsum</div><p>Lorem ipsum is simply dummy text and printing typesetting.</p><a class="link" href="https://larkfieldmedhub.example/careers">APPLY NOW</a></div>
<a class="btn" href="https://larkfieldmedhub.example/careers" style="left:525px;top:1162px;width:150px;height:45px">VIEW MORE</a>

<!-- ABOUT -->
<div class="about-bg"></div>
<div class="tile" style="left:60px;top:1484px;background:linear-gradient(180deg,#4ba9f3,#2e8ee6)">
  <svg viewBox="0 0 40 40" fill="none" stroke="#fff" stroke-width="2"><rect x="4" y="10" width="32" height="24" rx="2"/><path d="M14 10V6h12v4M20 16v12M14 22h12"/></svg>
  <h4>Emergency Care</h4><p>Lorem ipsum is simply.</p></div>
<div class="tile" style="left:60px;top:1672px;background:linear-gradient(180deg,#6dd5b2,#52bf98)">
  <svg viewBox="0 0 40 40" fill="none" stroke="#fff" stroke-width="2"><rect x="8" y="12" width="18" height="24" rx="2"/><path d="M11 6h12v6M17 20v8M13 24h8"/><circle cx="30" cy="30" r="5"/></svg>
  <h4>Online Pharmacy</h4><p>Lorem ipsum is simply.</p></div>
<div class="tile" style="left:232px;top:1394px;background:linear-gradient(180deg,#46bfe7,#2ca4d8)">
  <svg viewBox="0 0 40 40" fill="none" stroke="#fff" stroke-width="2"><rect x="4" y="12" width="20" height="14" rx="2"/><path d="M10 26l-4 5v-5M16 12V7h20v14h-6l-4 4v-4"/></svg>
  <h4>Consultation</h4><p>Lorem ipsum is simply.</p></div>
<div class="tile" style="left:232px;top:1582px;background:linear-gradient(180deg,#a77ee7,#8c65d7)">
  <svg viewBox="0 0 40 40" fill="none" stroke="#fff" stroke-width="2"><rect x="9" y="7" width="22" height="29" rx="2"/><path d="M15 5h10v5H15zM14 17h12M14 23h12M14 29h8"/></svg>
  <h4>Details Info</h4><p>Lorem ipsum is simply.</p></div>
<div class="tile" style="left:232px;top:1770px;background:linear-gradient(180deg,#f4669f,#e8437d)">
  <svg viewBox="0 0 40 40" fill="none" stroke="#fff" stroke-width="2"><rect x="4" y="8" width="32" height="24" rx="2"/><path d="M8 21h7l3-6 4 11 3-5h7"/></svg>
  <h4>Tracking</h4><p>Lorem ipsum is simply.</p></div>
<div class="tile" style="left:405px;top:1484px;background:linear-gradient(180deg,#97da7b,#7cc466)">
  <svg viewBox="0 0 40 40" fill="none" stroke="#fff" stroke-width="2"><path d="M10 4v10a7 7 0 0 0 14 0V4M17 21v6a7 7 0 0 0 14 0v-2"/><circle cx="31" cy="22" r="3"/></svg>
  <h4>Dedicated</h4><p>Lorem ipsum is simply.</p></div>
<div class="tile" style="left:405px;top:1672px;background:linear-gradient(180deg,#8e95f0,#7279dd)">
  <svg viewBox="0 0 40 40" fill="none" stroke="#fff" stroke-width="2"><circle cx="20" cy="20" r="16"/><path d="M14 12l4 4-2 3c1 3 3 5 6 6l3-2 4 4-3 3c-8-1-14-7-15-15z"/></svg>
  <h4>Support Patient</h4><p>Lorem ipsum is simply.</p></div>

<h2 class="abs about-title">ABOUT US</h2>
<p class="abs about-text" style="top:1530px">Lorem Ipsum is simply dummy text of the printing and typesetting industry. Lorem Ipsum has been the industry's standard dummy text ever since the 1500s, when an unknown printer took a galley of type and scrambled it to make a type specimen book. It has survived not only five centuries, but also the leap into electronic typesetting, remaining essentially unchanged.</p>
<p class="abs about-text" style="top:1688px">It was popularised in the 1960s with the release of Letraset sheets containing Lorem Ipsum passages, and more recently with desktop publishing software like Aldus PageMaker including versions of Lorem Ipsum.</p>
<a class="btn" href="#" style="left:637px;top:1804px;width:150px;height:45px">READ MORE</a>

<!-- BANNER -->
<div class="banner">
  <div class="circle"></div>
  <div class="rule"></div>
  <h2>LOREM IPSUM IS SIMPLY DUMMY TEXT</h2>
  <p>Lorem Ipsum is simply dummy text of the printing and typesetting industry. Lorem Ipsum has been the industry's standard dummy text ever since the 1500s.</p>
  <a class="btn" href="https://larkfieldmedhub.example/careers">APPLY NOW</a>
</div>

<!-- NEWS -->
<h2 class="section-title" style="top:2332px">LATEST NEWS</h2>
<article class="news" style="left:60px">
  <div class="img" role="img" aria-label="Patients waiting at a hospital reception desk"></div>
  <div class="date"><b>06</b><span>Aug</span></div>
  <h3>Lorem ipsum is simply dummt text and printing typesetting.</h3>
  <p>Lorem Ipsum is simply dummy text of the printing and typesetting industry. Lorem Ipsum has been the industry's standard dummy text ever...</p>
  <a class="link" href="#">READ MORE</a>
</article>
<article class="news" style="left:432px">
  <div class="img" role="img" aria-label="Lab technician working at a computer in a laboratory"></div>
  <div class="date"><b>05</b><span>Aug</span></div>
  <h3>Lorem ipsum is simply dummt text and printing typesetting.</h3>
  <p>Lorem Ipsum is simply dummy text of the printing and typesetting industry. Lorem Ipsum has been the industry's standard dummy text ever...</p>
  <a class="link" href="#">READ MORE</a>
</article>
<article class="news" style="left:803px">
  <div class="img" role="img" aria-label="Pharmacist in a white coat standing between pharmacy shelves"></div>
  <div class="date"><b>04</b><span>Aug</span></div>
  <h3>Lorem ipsum is simply dummt text and printing typesetting.</h3>
  <p>Lorem Ipsum is simply dummy text of the printing and typesetting industry. Lorem Ipsum has been the industry's standard dummy text ever...</p>
  <a class="link" href="#">READ MORE</a>
</article>

<!-- FOOTER -->
<svg class="abs" style="left:0;top:2880px" width="1200" height="434" viewBox="0 0 1200 434">
  <defs><linearGradient id="footGrad" x1="0" y1="0" x2="0" y2="1"><stop offset="0" stop-color="#dfe8f5"/><stop offset="1" stop-color="#f3f6fb"/></linearGradient></defs>
  <path d="M0 170 C300 90 600 80 880 20 C1000 -5 1120 10 1200 40 L1200 434 L0 434 Z" fill="url(#footGrad)"/>
</svg>
<div class="brand" style="left:60px;top:3114px"><span class="dot"></span><div>Larkfield<small>MEDICAL CENTER</small></div></div>
<span class="social" style="left:60px"></span>
<span class="social" style="left:98px"></span>
<span class="social" style="left:135px"></span>

<div class="footer-head" style="left:339px">Useful Links</div>
<a class="footer-link" style="left:339px;top:3094px">Home</a>
<a class="footer-link" style="left:339px;top:3132px">About</a>
<a class="footer-link" style="left:339px;top:3169px">Vacancies</a>
<a class="footer-link" style="left:339px;top:3207px">Contact Us</a>

<div class="footer-head" style="left:616px">Contact Info</div>
<svg class="abs" style="left:617px;top:3097px" width="12" height="16" viewBox="0 0 12 16" fill="none" stroke="#2a5fa3" stroke-width="1.6"><path d="M6 15s5-5 5-9A5 5 0 0 0 1 6c0 4 5 9 5 9z"/><circle cx="6" cy="6" r="1.8"/></svg>
<p class="footer-link" style="left:637px;top:3094px;width:225px;line-height:22.5px">Lorem ipsum is simply dummy text and printing.</p>
<svg class="abs" style="left:616px;top:3164px" width="14" height="14" viewBox="0 0 24 24" fill="#2a5fa3"><path d="M6.6 10.8a15 15 0 0 0 6.6 6.6l2.2-2.2c.3-.3.7-.4 1-.2 1.1.4 2.3.6 3.6.6.6 0 1 .4 1 1V20c0 .6-.4 1-1 1A17 17 0 0 1 3 4c0-.6.4-1 1-1h3.5c.6 0 1 .4 1 1 0 1.3.2 2.5.6 3.6.1.3 0 .7-.2 1z"/></svg>
<span class="footer-link" style="left:637px;top:3162px;color:#333;font-weight:500">555 018 2947</span>
<svg class="abs" style="left:616px;top:3210px" width="14" height="11" viewBox="0 0 14 11" fill="none" stroke="#2a5fa3" stroke-width="1.4"><rect x=".7" y=".7" width="12.6" height="9.6" rx="1"/><path d="M1 1l6 5 6-5"/></svg>
<span class="footer-link" style="left:637px;top:3207px">info@larkfieldmedical.example</span>

<div class="footer-head" style="left:894px">Newsletter</div>
<p class="footer-link" style="left:894px;top:3094px;width:240px;line-height:22.5px">Subscribe to stay with us and update our latest news , vacancies and etc...</p>
<div class="newsletter"><span>Enter email here...</span><div class="send"><svg width="18" height="18" viewBox="0 0 24 24" fill="#fff"><path d="M22 2L2 10l7 3 2 8 3-5 5 4z"/></svg></div></div>

<div class="abs" style="left:60px;top:3270px;width:1080px;height:1px;background:#cfd8e4"></div>
<p class="abs" style="left:0;top:3286px;width:1200px;text-align:center;font-size:11.5px;color:#666">© LARKFIELD MEDICAL CENTER – 2022. All Rights Reserved.</p>

</body>
</html>
```